Party Decoration Set Designs - Rose Gold theme - more example images just added

We are looking for a set of designs for a set of party decorations. It’s a Rose Gold colored theme. I have attached some photos of some glittery rose gold items that I think would go good with the theme. There are also some photos of full sets of decorations in other colors schemes to give an idea of what we are looking for.

We would like to have designs for the items below:

1- Happy Birthday Flag Banner- looking for something unique. Size- 5”X7” WXL

2- hanging swirl cards ( photo examples attached) 4”X6” approx. can be different sizes and shapes.

3- centerpiece designs- photo examples attached. Middle
Piece that’s says Happy Birthday should be 5”X 7” and the smaller surrounding pieces 3X5

4 - round candy stickers and candy wrappers. Examples below. .75 inch

The photos below are of products currently sold. We would like to be very similar to these but just a little different to make our own. And then to have a Happy Birthday banner created to match the theme.

Some of these example photos below are from different themes and colors But I included them because they are the complete set we want to create. First we will do a generic “Happy Birthday” Set with rose gold glitter theme and then later we will add the Sweet 16 birthday theme as well and 40th, 50th etc.

On the centerpieces where the example photos how a large “40”, we would like this to be a larger “Happy Birthday” design. Then surrounded by some smaller designs.
I look forward to receiving your ideas
Updates

Target Market(s)

Anyone looking for birthday Peru decorations for a female.

Font styles to use
Other font styles liked:
• Open to designer suggestion

Requirements
Must have
• Happy Birthday Banner, Hanging swirl cards, centerpiece cards, cake topper
Nice to have
• We are certainly open to any creative ideas.
Should not have
• I just now added some example images of a very good set of exactly what we want but its in a different theme. This is a black gold set and our requested design is more feminine and Rose Gold color

```html
<!DOCTYPE html>
<html lang="en">
<head>
<meta charset="utf-8">
<title>Rose Gold Glitter Birthday Theme Decoration</title>
<link rel="stylesheet" href="https://fonts.googleapis.com/css2?family=Montserrat:wght@400;600;900&family=Rye&family=Playfair+Display:wght@700&display=swap">
<style>
  :root {
    --ink: #111111;
    --paper: #ffffff;
    --blush-light: #fdf4f0;
    --blush-mid: #fbe4dc;
    --blush-deep: #f4c9bf;
    --rose-1: #f1c0b2;
    --rose-2: #d9917f;
    --rose-3: #c77a69;
    --rose-letter: #e0a797;
    --string: #f2b9b9;
  }
  * { margin: 0; padding: 0; box-sizing: border-box; }
  html, body { width: 1200px; height: 1008px; overflow: hidden; background: var(--paper); }
  .sheet { position: relative; width: 1200px; height: 1008px; background: var(--paper); font-family: "Montserrat", sans-serif; color: var(--ink); }
  .title-band {
    position: absolute; left: 0; top: 0; width: 1200px; height: 153px;
    background: linear-gradient(90deg, var(--blush-light) 0%, var(--blush-mid) 55%, var(--blush-deep) 100%);
  }
  .title-band h1 {
    position: absolute; left: 62px; top: 66px;
    font-weight: 600; font-size: 37.5px; letter-spacing: 0.2px; line-height: 1;
  }
  .option-label { position: absolute; font-family: "Montserrat", sans-serif; font-weight: 900; font-size: 22px; line-height: 1; }
  .option-desc { position: absolute; font-weight: 400; font-size: 22px; line-height: 1; }
  .label-one { left: 42px; top: 205px; }
  .desc-one { left: 41px; top: 247px; }
  .label-two { left: 50px; top: 585px; }
  .desc-two { left: 45px; top: 624px; }
  .banners { position: absolute; left: 0; top: 0; width: 1200px; height: 1008px; }
  .string { stroke: var(--string); stroke-width: 1.5; }
  .flag { fill: url(#glitter); }
  .flag-window { fill: var(--paper); }
  .badge { fill: var(--paper); }
  .letter-western { font-family: "Rye", serif; font-size: 92px; fill: var(--paper); text-anchor: middle; }
  .letter-serif { font-family: "Playfair Display", serif; font-weight: 700; font-size: 100px; fill: var(--rose-letter); text-anchor: middle; }
</style>
</head>
<body>
<div class="sheet">
  <header class="title-band"><h1>ROSE GOLD GLITTER BIRHTDAY THEME DECORATION</h1></header>

  <p class="option-label label-one">Option 1</p>
  <p class="option-desc desc-one">Happy Birthday Flag Banner - Size- 5”X7”</p>
  <p class="option-label label-two">Option 2</p>
  <p class="option-desc desc-two">Happy Birthday Flag Banner - Size- 5”X7”</p>

  <svg class="banners" viewBox="0 0 2000 1680" role="img" aria-label="Rose gold glitter pennant banners spelling Happy Birthday">
    <defs>
      <linearGradient id="glitter" x1="0" y1="0" x2="1" y2="1">
        <stop offset="0" stop-color="var(--rose-1)"/>
        <stop offset="0.45" stop-color="var(--rose-2)"/>
        <stop offset="0.75" stop-color="var(--rose-3)"/>
        <stop offset="1" stop-color="var(--rose-1)"/>
      </linearGradient>
      <polygon id="pennant" class="flag" points="0,0 182,0 92,184"/>
      <polygon id="window" class="flag-window" points="62,0 160,0 92,168"/>
      <g id="badge"><circle class="badge" cx="92" cy="66" r="42" role="img" aria-label="Happy Birthday script badge with stars"/></g>
    </defs>

    <!-- Option 1, row 1 -->
    <line class="string" x1="377" y1="513" x2="1853" y2="513"/>
    <g transform="translate(476 513)"><use href="#pennant"/><use href="#badge"/></g>
    <g transform="translate(660 513)"><use href="#pennant"/><text class="letter-western" x="90" y="95">H</text></g>
    <g transform="translate(844 513)"><use href="#pennant"/><text class="letter-western" x="90" y="95">A</text></g>
    <g transform="translate(1028 513)"><use href="#pennant"/><text class="letter-western" x="90" y="95">P</text></g>
    <g transform="translate(1212 513)"><use href="#pennant"/><text class="letter-western" x="90" y="95">P</text></g>
    <g transform="translate(1394 513)"><use href="#pennant"/><text class="letter-western" x="90" y="95">Y</text></g>
    <g transform="translate(1576 513)"><use href="#pennant"/><use href="#badge"/></g>

    <!-- Option 1, row 2 -->
    <line class="string" x1="143" y1="735" x2="1907" y2="735"/>
    <g transform="translate(204 735)"><use href="#pennant"/><text class="letter-western" x="90" y="97">B</text></g>
    <g transform="translate(387 735)"><use href="#pennant"/><text class="letter-western" x="90" y="97">I</text></g>
    <g transform="translate(571 735)"><use href="#pennant"/><text class="letter-western" x="90" y="97">R</text></g>
    <g transform="translate(755 735)"><use href="#pennant"/><text class="letter-western" x="90" y="97">T</text></g>
    <g transform="translate(939 735)"><use href="#pennant"/><text class="letter-western" x="90" y="97">H</text></g>
    <g transform="translate(1122 735)"><use href="#pennant"/><text class="letter-western" x="90" y="97">D</text></g>
    <g transform="translate(1305 735)"><use href="#pennant"/><text class="letter-western" x="90" y="97">A</text></g>
    <g transform="translate(1488 735)"><use href="#pennant"/><text class="letter-western" x="90" y="97">Y</text></g>
    <g transform="translate(1672 735)"><use href="#pennant"/><use href="#badge"/></g>

    <!-- Option 2, row 1 -->
    <line class="string" x1="384" y1="1140" x2="1860" y2="1140"/>
    <g transform="translate(483 1140)"><use href="#pennant"/><use href="#badge"/></g>
    <g transform="translate(668 1140)"><use href="#pennant"/><use href="#window"/><text class="letter-serif" x="92" y="88">H</text></g>
    <g transform="translate(852 1140)"><use href="#pennant"/><use href="#window"/><text class="letter-serif" x="96" y="88">A</text></g>
    <g transform="translate(1036 1140)"><use href="#pennant"/><use href="#window"/><text class="letter-serif" x="98" y="88">P</text></g>
    <g transform="translate(1220 1140)"><use href="#pennant"/><use href="#window"/><text class="letter-serif" x="98" y="88">P</text></g>
    <g transform="translate(1404 1140)"><use href="#pennant"/><use href="#window"/><text class="letter-serif" x="90" y="88">Y</text></g>
    <g transform="translate(1588 1140)"><use href="#pennant"/><use href="#badge"/></g>

    <!-- Option 2, row 2 -->
    <line class="string" x1="150" y1="1362" x2="1915" y2="1362"/>
    <g transform="translate(211 1362)"><use href="#pennant"/><use href="#window"/><text class="letter-serif" x="94" y="92">B</text></g>
    <g transform="translate(394 1362)"><use href="#pennant"/><use href="#window"/><text class="letter-serif" x="94" y="92">I</text></g>
    <g transform="translate(578 1362)"><use href="#pennant"/><use href="#window"/><text class="letter-serif" x="94" y="92">R</text></g>
    <g transform="translate(762 1362)"><use href="#pennant"/><use href="#window"/><text class="letter-serif" x="92" y="92">T</text></g>
    <g transform="translate(946 1362)"><use href="#pennant"/><use href="#window"/><text class="letter-serif" x="92" y="92">H</text></g>
    <g transform="translate(1128 1362)"><use href="#pennant"/><use href="#window"/><text class="letter-serif" x="92" y="92">D</text></g>
    <g transform="translate(1310 1362)"><use href="#pennant"/><use href="#window"/><text class="letter-serif" x="92" y="92">A</text></g>
    <g transform="translate(1493 1362)"><use href="#pennant"/><use href="#window"/><text class="letter-serif" x="90" y="92">Y</text></g>
    <g transform="translate(1677 1362)"><use href="#pennant"/><use href="#badge"/></g>
  </svg>
</div>
</body>
</html>
```